Residential Remodeling Contractor needs updated business card

I need a new design for my business card.
Name of the company is Brookfell Construction. I need a card that commands presence, strength, integrity. I have been in business for 28 years. I am a Residential Remodeling Contractor that covers all aspects of a residential remodel and build.

```html
<!DOCTYPE html>
<html lang="en">
<head>
<meta charset="UTF-8">
<title>Brookfell Construction – Business Card</title>
<link href="https://fonts.googleapis.com/css2?family=Cinzel:wght@500&family=Montserrat:wght@400;700&display=swap" rel="stylesheet">
<style>
  :root {
    --navy: #223f7e;
    --white: #ffffff;
    --mark-tint: #dfe4f0;
    --backdrop: #b4b4b4;
    --ink: #223f7e;
    --muted: #2b3a5c;
    --body-text: #1c2440;
  }
  * { box-sizing: border-box; margin: 0; padding: 0; }
  html, body { width: 1200px; height: 900px; overflow: hidden; }
  body {
    background: var(--backdrop);
    position: relative;
    font-family: "Montserrat", Arial, sans-serif;
  }
  .card {
    position: absolute;
    width: 640px;
    height: 366px;
    background: var(--navy);
    overflow: hidden;
    box-shadow: 0 6px 18px rgba(0,0,0,0.25);
  }
  .card--front { left: 70px; top: 60px; }
  .card--back { left: 490px; top: 474px; }

  .brand-mark {
    background: var(--mark-tint);
    width: 72px;
    height: 72px;
    flex: none;
  }
  .wordmark {
    font-family: "Cinzel", Georgia, serif;
    font-weight: 500;
    color: var(--white);
    line-height: 1.05;
    letter-spacing: 1px;
  }

  .card--front .brand {
    position: absolute;
    left: 50px;
    top: 40px;
    display: flex;
    align-items: center;
    gap: 26px;
  }
  .card--front .wordmark { font-size: 50px; }

  .card--back .brand {
    position: absolute;
    left: 0; right: 0;
    top: 0; bottom: 0;
    display: flex;
    align-items: center;
    justify-content: center;
    gap: 24px;
  }
  .card--back .wordmark { font-size: 52px; }

  .info-band {
    position: absolute;
    left: 0; right: 0;
    top: 180px;
    height: 124px;
    background: var(--white);
    display: flex;
    align-items: center;
    padding-left: 56px;
    padding-right: 40px;
  }
  .person {
    text-align: right;
    padding-right: 22px;
    white-space: nowrap;
  }
  .person__name {
    font-weight: 700;
    font-size: 24px;
    color: var(--ink);
  }
  .person__role {
    font-size: 14px;
    color: var(--muted);
    margin-top: 4px;
  }
  .divider {
    width: 2px;
    height: 82px;
    background: var(--ink);
    flex: none;
  }
  .contacts {
    list-style: none;
    padding-left: 18px;
    display: flex;
    flex-direction: column;
    gap: 9px;
  }
  .contacts li {
    display: flex;
    align-items: center;
    gap: 10px;
    font-size: 14px;
    color: var(--body-text);
    white-space: nowrap;
  }
  .contacts svg { width: 18px; height: 18px; flex: none; }
</style>
</head>
<body>

  <section class="card card--front" aria-label="Business card front">
    <div class="brand">
      <div class="brand-mark" role="img" aria-label="Brand mark area"></div>
      <div class="wordmark">Brookfell<br>Construction</div>
    </div>

    <div class="info-band">
      <div class="person">
        <div class="person__name">Daniel Harlow</div>
        <div class="person__role">Owner</div>
      </div>
      <div class="divider"></div>
      <ul class="contacts">
        <li>
          <svg viewBox="0 0 20 20" aria-hidden="true"><path fill="#223f7e" d="M3 8c0-3 3-5 7-5s7 2 7 5l-3 1-1-2H7L6 9 3 8zm3 2h8l2 7H4l2-7zm4 1.5a2 2 0 1 0 0 4 2 2 0 0 0 0-4z"/></svg>
          555.204.7318
        </li>
        <li>
          <svg viewBox="0 0 20 20" aria-hidden="true"><rect x="2" y="4" width="16" height="12" fill="#223f7e"/><path d="M2 4l8 7 8-7" fill="none" stroke="#fff" stroke-width="1.5"/></svg>
          info@brookfellconstruction.com
        </li>
        <li>
          <svg viewBox="0 0 20 20" aria-hidden="true"><circle cx="10" cy="10" r="8" fill="#223f7e"/><path d="M2 10h16M10 2c3 3 3 13 0 16M10 2c-3 3-3 13 0 16" fill="none" stroke="#fff" stroke-width="1.2"/></svg>
          www.brookfellconstruction.com
        </li>
      </ul>
    </div>
  </section>

  <section class="card card--back" aria-label="Business card back">
    <div class="brand">
      <div class="brand-mark" role="img" aria-label="Brand mark area"></div>
      <div class="wordmark">Brookfell<br>Construction</div>
    </div>
  </section>

</body>
</html>
```